Kelvar Systems Website

Website design for our company: Kelvar Systems.
The website should look fresh and IT focused. Please have a look at http://www.kelvarsystems.net.au/ for our current design. We want something fresh and new, professional looking, in WordPress so we can easily make changes.

Industry/Entity Type

It Company

```html
<!DOCTYPE html>
<html lang="en">
<head>
<meta charset="utf-8">
<title>Kelvar Systems</title>
<link href="https://fonts.googleapis.com/css2?family=Open+Sans:ital,wght@0,300;0,400;0,600;0,700;1,400&display=swap" rel="stylesheet">
<style>
:root{
  --green:#13b158;
  --green-dark:#0e9c4b;
  --blue:#1a6fc4;
  --blue-bar:#2c86d2;
  --title-blue:#2a8ad6;
  --text:#333;
  --muted:#8a8a8a;
  --light:#f3f3f3;
  --panel:#e9e9e9;
  --footer:#353a41;
  --footer-text:#7c828a;
  --white:#fff;
}
*{margin:0;padding:0;box-sizing:border-box}
html,body{width:1024px;height:1200px;overflow:hidden}
body{font-family:'Open Sans',sans-serif;background:var(--light);position:relative;color:var(--text)}
.header{position:absolute;left:0;top:0;width:1024px;height:92px;background:linear-gradient(#17b85d,#0fa850);border-bottom:5px solid var(--blue)}
.brand{position:absolute;left:140px;top:8px;width:142px;height:70px;background:var(--white);border-radius:4px;display:flex;align-items:center;justify-content:center;gap:6px;font-weight:700;font-size:15px;color:var(--blue)}
.brand i{width:12px;height:12px;border-radius:50%;background:var(--blue)}
.callus{position:absolute;left:562px;top:25px;color:var(--white);font-weight:700;font-size:12px;display:flex;align-items:center;gap:6px}
.search{position:absolute;left:727px;top:20px;width:161px;height:24px;background:var(--white);border:1px solid #bde3c8;font-size:9px;color:#999;padding:6px 0 0 28px}
.search svg{position:absolute;left:8px;top:5px}
.nav{position:absolute;top:51px;left:315px;display:flex;list-style:none}
.nav li{color:var(--white);font-size:12px;height:36px;line-height:36px;margin-right:0}
.nav li.active{background:linear-gradient(#3a95e0,#1a6fc4);width:80px;text-align:center;font-weight:700}
.hero{position:absolute;left:0;top:92px;width:1024px;height:378px;background:linear-gradient(115deg,#2f86d0 0%,#8cc6ee 18%,#e8eef3 38%,#f4f6f8 60%,#c9dced 80%,#3b84c8 100%)}
.hero-photo{position:absolute;left:160px;top:18px;width:290px;height:360px;border-radius:140px 140px 0 0;background:linear-gradient(#d9d4cf,#8a8d93)}
.hero h1{position:absolute;left:520px;top:108px;font-weight:300;font-size:30px;line-height:39px;color:var(--title-blue)}
.btn{display:inline-block;border:1px solid #bbb;border-radius:2px;background:linear-gradient(#fff,#ececec);color:#666;font-size:11px;height:31px;line-height:29px;padding:0 16px;box-shadow:0 1px 2px rgba(0,0,0,.15)}
.hero .btn{position:absolute;left:523px;top:207px;width:88px;text-align:center;padding:0}
.card{position:absolute;top:437px;height:315px;background:var(--white);border-radius:3px;box-shadow:0 1px 3px rgba(0,0,0,.1)}
.card h2{font-weight:300;font-size:20px;color:#333}
.about{left:140px;width:233px;padding:22px 16px}
.about .pic{margin-top:14px;width:200px;height:101px;background:linear-gradient(#c8d4df,#5b6672)}
.about p{margin-top:16px;font-size:11.5px;line-height:16px;color:var(--muted)}
.about .btn,.services .btn{position:absolute;left:14px;top:266px}
.services{left:395px;width:233px;padding:22px 27px}
.services ul{list-style:none;margin-top:12px}
.services li{font-size:11.5px;color:var(--muted);height:24px;display:flex;align-items:center;gap:8px}
.services li i{width:8px;height:8px;border-radius:50%;border:2.5px solid #bbb}
.remote{left:650px;width:233px;overflow:hidden}
.remote-head{height:107px;background:linear-gradient(#1fc064,#10a650);border-bottom:2px solid #0c8d44;padding:25px 0 0 20px;color:var(--white)}
.remote-head .ic{position:absolute;left:19px;top:25px;width:50px;height:50px;border-radius:5px;background:var(--green-dark);display:flex;align-items:center;justify-content:center}
.remote-head h2{position:absolute;left:78px;top:22px;color:var(--white);font-size:20px}
.remote-head p{position:absolute;left:81px;top:49px;font-size:9px;line-height:14.5px;color:#0b4a25}
.code{position:absolute;left:19px;top:130px;width:198px;height:38px;border:1px solid #ccc;border-radius:2px;font-size:10px;color:#bbb;padding:11px 0 0 46px}
.code svg{position:absolute;left:17px;top:11px}
.remote .btn{position:absolute;left:19px;top:181px;width:88px;text-align:center;padding:0}
.line{position:absolute;left:0;width:233px;border-top:1px solid #e6e6e6;font-size:11px;color:var(--muted);padding:12px 20px}
.line a{color:var(--title-blue);text-decoration:none}
.section-title{position:absolute;top:784px;font-weight:300;font-size:20px;color:#333}
.quote{position:absolute;left:140px;top:822px;width:488px;height:106px;background:var(--panel);padding:17px 20px;font-style:italic;font-size:11.5px;line-height:21px;color:#888}
.quote-tail{position:absolute;left:568px;top:928px}
.cite{position:absolute;left:224px;top:940px;font-size:10px;font-style:italic;color:#777}
.client{position:absolute;background:#d8d8d8;display:flex;align-items:center;justify-content:center;font-size:13px;font-weight:600;color:var(--white)}
.client.alt{background:none;color:#999}
.footer{position:absolute;left:0;top:999px;width:1024px;height:166px;background:var(--footer)}
.f-brand{position:absolute;left:135px;top:31px;width:150px;height:76px;background:#4d535b;border-radius:4px;display:flex;align-items:center;justify-content:center;gap:6px;color:#8d939a;font-weight:700;font-size:14px}
.f-brand i{width:11px;height:11px;border-radius:50%;background:#8d939a}
.f-col{position:absolute;top:31px;font-size:9.5px;color:var(--footer-text)}
.f-col h3{font-size:10px;font-weight:400;color:#b8bcc1;margin-bottom:14px}
.f-col p{line-height:18.5px}
.f-col .on{color:var(--white)}
.bottom{position:absolute;left:0;top:1165px;width:1024px;height:35px;background:var(--blue-bar);color:var(--white);font-size:8.5px;line-height:35px}
</style>
</head>
<body>
<header class="header">
  <div class="brand"><i></i>Kelvar Systems</div>
  <div class="callus"><svg width="14" height="14" viewBox="0 0 14 14"><path d="M3 1l2 3-1.5 1.5a8 8 0 0 0 5 5L10 9l3 2-1 2c-6 0-11-5-11-11z" fill="none" stroke="#c9f0d6" stroke-width="1.3"/></svg>Call us: +61 400 555 017</div>
  <div class="search"><svg width="14" height="14" viewBox="0 0 14 14"><circle cx="6" cy="6" r="4.5" fill="none" stroke="#7fcf97" stroke-width="1.3"/><path d="M9.5 9.5L13 13" stroke="#7fcf97" stroke-width="1.3"/></svg>Search</div>
  <ul class="nav">
    <li class="active">Home</li><li style="margin-left:21px">Services</li><li style="margin-left:45px">Support</li><li style="margin-left:41px">Clients</li><li style="margin-left:45px">Testimonial</li><li style="margin-left:50px">About</li><li style="margin-left:42px">Contact</li>
  </ul>
</header>

<section class="hero">
  <div class="hero-photo" role="img" aria-label="Photo of a smiling businesswoman in front of a blue globe"></div>
  <h1>We Bring Your Business<br>Forward with Our Solutions</h1>
  <span class="btn">Contact Us</span>
</section>

<article class="card about">
  <h2>About Kelvar Systems</h2>
  <div class="pic" role="img" aria-label="Photo of a business team in a meeting"></div>
  <p>Kelvar Systems is an Adelaide based company with a single objective - to excel in the support and service of all computer and IT needs.</p>
  <span class="btn">Read More</span>
</article>

<article class="card services">
  <h2>Our Services</h2>
  <ul>
    <li><i></i>On-site Service</li><li><i></i>Remote Desktop Support</li><li><i></i>Medical IT Service</li><li><i></i>Pharmacy IT Service</li><li><i></i>Website Design</li><li><i></i>Disaster Recovery</li><li><i></i>Hardware/ Software supply</li><li><i></i>Consumables</li>
  </ul>
  <span class="btn">Read More</span>
</article>

<article class="card remote">
  <div class="remote-head">
    <div class="ic"><svg width="30" height="24" viewBox="0 0 30 24"><ellipse cx="12" cy="9" rx="10" ry="7" fill="#fff"/><ellipse cx="19" cy="13" rx="9" ry="6" fill="#e6f7ec"/><path d="M6 14l-2 5 6-3z" fill="#fff"/></svg></div>
    <h2>Remote Support</h2>
    <p>Enter Your 6 digit code to<br>connect our support</p>
  </div>
  <div class="code"><svg width="12" height="15" viewBox="0 0 12 15"><rect x="1" y="6" width="10" height="8" fill="none" stroke="#2a8ad6" stroke-width="1.3"/><path d="M3 6V4a3 3 0 0 1 6 0" fill="none" stroke="#2a8ad6" stroke-width="1.3"/></svg>******</div>
  <span class="btn">Connect</span>
  <div class="line" style="top:229px">Phone: (+61)1800.555.0190</div>
  <div class="line" style="top:271px">E-mail: <a>info@kelvarsystems.com</a></div>
</article>

<h2 class="section-title" style="left:154px">Testimonials</h2>
<blockquote class="quote">"I have always found the team extremely helpful with their advice over the phone. They also have the ability to access our computers remotely, and can rectify most problems quite swiftly. I have no hesitation in recommending Kelvar Systems for all of your IT needs."</blockquote>
<svg class="quote-tail" width="24" height="20" viewBox="0 0 24 20"><path d="M0 0h24L0 20z" fill="#e9e9e9"/></svg>
<p class="cite"><b style="font-style:normal;color:#999">❞</b>&nbsp; Daniel Morrow of Harbourline Pharmacy, Seacliff</p>

<h2 class="section-title" style="left:660px">Our Clients</h2>
<div class="client" style="left:650px;top:822px;width:127px;height:65px">Brightway Chemists</div>
<div class="client alt" style="left:797px;top:822px;width:93px;height:68px;text-align:center">Northgate Pharmacy</div>
<div class="client" style="left:651px;top:901px;width:239px;height:62px;background:#e2e2e2;color:#999">Corran &amp; Pell Health</div>

<footer class="footer">
  <div class="f-brand"><i></i>Kelvar Systems</div>
  <div class="f-col" style="left:329px">
    <h3>NAVIGATION</h3>
    <div style="display:flex;gap:40px"><p>Home<br><span class="on">Clients</span><br>Services<br>Support</p><p>Testimonials<br>About<br>Contact Us</p></div>
  </div>
  <div class="f-col" style="left:521px"><h3>WHERE WE ARE</h3><p>PO Box 40512<br>Fernhill Rd, Adelaide<br>South Australia 5000</p></div>
  <div class="f-col" style="left:714px"><h3>CONTACT US</h3><p>Phone: (08) 555 0142<br>support@kelvarsystems.com</p></div>
</footer>
<div class="bottom"><span style="position:absolute;left:136px">COPYRIGHT - 2014 - KELVAR SYSTEMS</span><span style="position:absolute;left:717px">PRIVACY POLICY | SITEMAP</span></div>
</body>
</html>
```